Home page design for community learning promoters' website

There are about 3,000 community learning centers where people from underprivileged / marginalized communities can learn about basic technology topics like: how to use computers, how to use Internet (create an email, join and use social networks, etc.), how to use Word, Excel, PowerPoint, and so on... This is very useful for them because it gives them opportunities to find / get a better job and improve their standard of living.

Well, this website is an online community for those men and women (the promoters) who are responsible for leading the centers. They coordinate all the activities in the centers and they teach their students.

The website has two main objectives: 1) create culture about the importance of the promoters role in their communities and 2) create a place where promoters can learn, take online courses and share best practices.

The first objective is the "public" part of the website (homepage and public information) and the second one is the "private" part which is a pinwheel like online community (accessible only for registered users).

What we need is a fresh and modern visual design for 1) "public" homepage and 2) "private" homepage. I am attaching some mockups for the homepage "public" part (two different options) and for the main page of the "private" part (the pinwheel like online community). This doesn't mean that your design should be like those mockups, but they could be a guide for you to get ideas and better understend the website objectives. What we need is innovation.

The project scope is to design the home page for the "public" part and the home page for the "private" part. If you have any question, please ask me.

Target Market(s)

Target market (promoters) are 20-40 years old, they work from 4 to 8 hours in the centers and their connections are mainly satellital 256Kb/s

Industry/Entity Type

Internet

Requirements
Must have
• Spanish labeling. Find below what homepage must have. I include english / spanish versions. For sample text you can use "lorem ipsum". If you need help with spanish tranlations you can ask me.

The homepage must have:

Links / menu to main sections:
- Who we are / Quiénes somos
- What we do / Qué hacemos
- Our impact / Nuestro impacto
- Enter now! / ¡Ingresa ahora!

Benefits that the site offer to the promoters (why they should join the online community). Call-to-action should be "Join now / Regístrate ahora"
- Get trained (Take online courses and get access to more than 450 learning resources) / Capacítate (Toma cursos en línea y accede a más de 450 recursos de aprendizaje)
- Get certified (Approve the course and become a certified promoter) / Certifícate (Aprueba el curso y conviértete en un promotor certificado)
- Connect (Connect and work with more than 3,000 promoters around the country) / Conéctate (Conéctate y colabora con más de 3,000 promotores de todo el país)
- Share (Learn and share information with other promoters) / Comparte (Aprende y comparte información con otros promotores)

Links / blocks / menus to secondary sections:
- Success stories / Historias de éxito
- Events and contests / Concursos y eventos
- News or Featured news / Noticias destacadas
- Follow us on... (social networks like pinwheel, glimmo, quorvaSt, etc.) / Síguenos en...
- Frequently asked questions / Preguntas frecuentes
- Contact us / Contáctanos
- Site map / Mapa del sitio
- Privacy policy / Políticas de privacidad
- Terms and conditions of use / Términos y condiciones de uso

Also should include statistics like:
- More that 3,000 promoters / Más de 3,000 promotores
- More than 850 learning resources / Más de 850 recursos de aprendizaje
- More than 450,000 students / Más de 450,000 estudiantes

```html
<!DOCTYPE html>
<html lang="es">
<head>
<meta charset="utf-8">
<title>Promotores – Inicio</title>
<link rel="stylesheet" href="https://fonts.googleapis.com/css2?family=Open+Sans:wght@400;600;700&family=Roboto+Condensed:wght@400;700&display=swap">
<style>
:root{
  --green:#1f7a2e;
  --green-dark:#0d5a1c;
  --green-title:#1c8a2c;
  --yellow:#f7bd12;
  --blue:#0f4a7a;
  --nav:#4a4a4a;
  --nav-dark:#333;
  --text:#333;
  --muted:#555;
  --footer:#262626;
  --footer-line:#3a3a3a;
  --lime:#6a9a22;
  --band:#f1f1f1;
}
*{margin:0;padding:0;box-sizing:border-box}
html,body{width:795px;height:1200px;overflow:hidden;background:#fff}
body{position:relative;font-family:"Open Sans",sans-serif;color:var(--text)}
.abs{position:absolute}

/* header */
.brand{left:68px;top:26px;display:flex;align-items:center;gap:8px;font-size:22px;color:#444;letter-spacing:.5px}
.brand-dot{width:22px;height:22px;border-radius:50%;background:var(--green)}
.register{left:475px;top:31px;font-weight:700;font-size:14px;color:#333}
.login{left:566px;top:20px;width:160px;height:40px;border-radius:6px;background:linear-gradient(#1e8a33,var(--green-dark));border:2px solid #d8e8d8;color:#fff;font-size:17px;display:flex;align-items:center;justify-content:center;gap:6px;letter-spacing:.3px}

/* nav */
.nav{left:0;top:83px;width:795px;height:34px;background:linear-gradient(#595959,var(--nav-dark));display:flex}
.nav a{color:#fff;text-decoration:none;font-size:16px;line-height:34px;position:absolute;top:0}
.nav .sep{position:absolute;top:8px;width:1px;height:20px;background:#777}
.promo-tab{left:600px;top:78px;width:104px;height:44px;background:var(--yellow);color:#222;font-weight:700;font-size:13px;display:flex;align-items:center;justify-content:center;box-shadow:0 1px 3px rgba(0,0,0,.3)}

/* hero */
.hero{left:0;top:117px;width:795px;height:309px;background:linear-gradient(110deg,#6a7d8e 0%,#8a7260 35%,#b89a7c 55%,#4f86b8 80%,#2b6aa0 100%)}
.quote{left:77px;top:181px;width:279px;height:117px;background:rgba(30,30,30,.72);border-radius:6px;color:#fff;padding:14px 12px 0 13px}
.quote p{font-size:16px;line-height:23px;font-weight:600}
.quote .by{position:absolute;right:8px;bottom:8px;color:var(--yellow);font-size:11px}
.arrow{top:236px;width:42px;height:42px;border-radius:50%;background:#fff;display:flex;align-items:center;justify-content:center;box-shadow:0 1px 3px rgba(0,0,0,.3)}

/* stats */
.stats{left:0;top:426px;width:795px;height:104px;background:linear-gradient(#f7f7f7,var(--band));border-bottom:2px solid #ddd}
.pill{top:441px;width:144px;height:71px;border-radius:36px;color:#fff;border:3px solid #eee;box-shadow:0 2px 4px rgba(0,0,0,.25)}
.pill .num{position:absolute;left:50px;top:10px;font-size:24px;font-weight:700;line-height:26px}
.pill .lbl{position:absolute;left:49px;top:37px;font-size:13px;color:#222}
.pill .ico{position:absolute;left:2px;top:10px;width:44px;height:44px;border-radius:10px}
.p-green{left:97px;background:radial-gradient(circle at 50% 30%,#2fa83e,var(--green))}
.p-yellow{left:337px;background:radial-gradient(circle at 50% 30%,#ffd04a,var(--yellow))}
.p-blue{left:546px;background:radial-gradient(circle at 50% 30%,#1e6aa6,var(--blue))}
.p-yellow .num{color:#fff}

/* content */
.h2{font-family:"Roboto Condensed",sans-serif;font-weight:700;font-size:21px;color:#444}
.h2 em{font-style:normal;color:var(--green-title)}
.divider{left:425px;top:562px;width:1px;height:425px;background:#ddd}
.thumb{border:2px solid #ccc;outline:1px solid #eee}
.play{position:absolute;left:50%;top:50%;width:28px;height:28px;margin:-14px 0 0 -14px;background:#f2f2f2;opacity:.9}
.story-t{font-size:14px;letter-spacing:1px;line-height:15px;color:#222;width:180px}
.story-p{font-size:9.5px;line-height:13.5px;color:#555;width:176px}
.news .date{font-size:9px;color:var(--green-title);font-weight:600}
.news .t{font-size:9.5px;font-weight:700;line-height:12px;color:#222;margin-top:5px;width:140px}
.news .p{font-size:8.5px;line-height:13.3px;color:#555;margin-top:5px;width:140px}
.news .more{display:inline-block;margin-top:5px;background:#333;color:#fff;font-size:7.5px;font-weight:700;padding:1px 4px}
.social{left:67px;top:907px;display:flex;gap:11px}
.social span{display:flex;align-items:center;gap:4px;font-size:11px;font-weight:600;color:#444}
.social i{width:30px;height:30px;border-radius:50%;display:block}

/* footer */
.footer{left:0;top:1013px;width:795px;height:137px;background:var(--footer)}
.fcol{top:1029px;width:104px}
.fcol div{font-size:9.5px;font-weight:600;color:#eee;height:18.6px;line-height:18px;border-bottom:1px solid var(--footer-line);padding-left:14px;position:relative}
.fcol div::before{content:"";position:absolute;left:3px;top:7px;width:4px;height:4px;border:1px solid #ccc;border-radius:50%}
.fcol div.active{background:#333}
.bottom{left:0;top:1150px;width:795px;height:50px;background:var(--lime);color:#fff;font-size:9px;text-align:center;padding-top:12px;line-height:12px}
</style>
</head>
<body>

<header>
  <div class="abs brand"><span class="brand-dot"></span>Company</div>
  <div class="abs register">Registrarme</div>
  <div class="abs login">Iniciar Sesion
    <svg width="12" height="10" viewBox="0 0 12 10"><path d="M1 1l4 4-4 4M6 1l4 4-4 4" stroke="#fff" stroke-width="1.5" fill="none"/></svg>
  </div>
</header>

<nav class="abs nav">
  <a style="left:71px">Who We Are</a><span class="sep" style="left:186px"></span>
  <a style="left:219px">Born</a><span class="sep" style="left:285px"></span>
  <a style="left:314px">Features</a><span class="sep" style="left:410px"></span>
  <a style="left:438px">Our Impact</a><span class="sep" style="left:550px"></span>
</nav>
<div class="abs promo-tab">Say Promotor</div>

<section class="abs hero" role="img" aria-label="Photo of young students gathered around computer monitors in a classroom"></section>
<div class="abs quote">
  <p>“ The developer development aid Your Community, earning respect personal satisfaction ”</p>
  <span class="by">Dr. Mateo Arriaga</span>
</div>
<div class="abs arrow" style="left:13px"><svg width="18" height="16" viewBox="0 0 18 16"><path d="M9 1L2 8l7 7M16 1L9 8l7 7" stroke="#333" stroke-width="2" fill="none"/></svg></div>
<div class="abs arrow" style="left:738px"><svg width="18" height="16" viewBox="0 0 18 16"><path d="M2 1l7 7-7 7M9 1l7 7-7 7" stroke="#333" stroke-width="2" fill="none"/></svg></div>

<section class="abs stats"></section>
<div class="abs pill p-green"><span class="ico" role="img" aria-label="Illustration of two promoters" style="background:#b2704a"></span><span class="num">+2,800</span><span class="lbl">promotores</span></div>
<div class="abs pill p-yellow"><span class="ico" role="img" aria-label="Illustration of a stack of books" style="background:#2c7ac4"></span><span class="num">+2,800</span><span class="lbl">promotores</span></div>
<div class="abs pill p-blue"><span class="ico" role="img" aria-label="Illustration of a graduation cap" style="background:#111"></span><span class="num">+2,800</span><span class="lbl" style="color:#cde">promotores</span></div>

<h2 class="abs h2" style="left:67px;top:555px"><em>Historias</em>&nbsp; De Exito</h2>
<div class="abs divider"></div>
<h2 class="abs h2" style="left:434px;top:556px"><em>Destacado</em> En E-Comunidad</h2>

<div class="abs thumb" style="left:68px;top:593px;width:170px;height:112px;background:linear-gradient(120deg,#6b4e3d,#b9a3c9 50%,#d8d8d8)" role="img" aria-label="Video still of a student at a computer"><span class="play"></span></div>
<div class="abs story-t" style="left:243px;top:591px">simply dummy text of the printing</div>
<p class="abs story-p" style="left:243px;top:626px">simply dummy text of the printing and typesetting industry. Lorem Ipsum has been the industry's standard dummy text ever since the 1500s,</p>

<div class="abs thumb" style="left:68px;top:737px;width:170px;height:112px;background:linear-gradient(110deg,#8a6a48,#e2d6c2 50%,#6a4a7a)" role="img" aria-label="Video still of a student in a library"><span class="play"></span></div>
<div class="abs story-t" style="left:243px;top:737px">simply dummy text of the printing</div>
<p class="abs story-p" style="left:243px;top:772px">simply dummy text of the printing and typesetting industry. Lorem Ipsum has been the Ipsum has been the industry's industry's standard dummy text ever since the 1500s,</p>

<h2 class="abs h2" style="left:67px;top:874px"><em>Connect</em> with Us</h2>
<div class="abs social">
  <span><i style="background:#2ea3dc"></i>glimmo</span>
  <span><i style="background:#3a5a98"></i>pinwheel</span>
  <span><i style="background:#c0392b"></i>plusra</span>
  <span><i style="background:#ee6b1e"></i>feed</span>
</div>

<div class="abs thumb" style="left:436px;top:592px;width:138px;height:115px;background:linear-gradient(130deg,#6a5a50,#c24a6a 50%,#9a9a9a)" role="img" aria-label="Photo of students working on laptops"></div>
<div class="abs news" style="left:582px;top:593px">
  <div class="date">13 July, 2013</div>
  <div class="t">simply dummy text printing typesetting.</div>
  <div class="p">simply dummy text of the printing and typesetting industry. Lorem Ipsum has been the industry's standard dummy text.</div>
  <span class="more">Learn More ›</span>
</div>

<div class="abs thumb" style="left:436px;top:726px;width:138px;height:115px;background:linear-gradient(130deg,#e8e8e8,#c98a6a 45%,#e04a8a 75%,#7ab04a)" role="img" aria-label="Photo of a smiling group of students"></div>
<div class="abs news" style="left:582px;top:727px">
  <div class="date">13 July, 2013</div>
  <div class="t">simply dummy text printing typesetting.</div>
  <div class="p">simply dummy text of the printing and typesetting industry. Lorem Ipsum has been the industry's standard dummy text.</div>
  <span class="more">Learn More ›</span>
</div>

<div class="abs thumb" style="left:436px;top:860px;width:138px;height:115px;background:linear-gradient(130deg,#f4f4f4,#e8d84a 45%,#7a4a3a 75%,#eee)" role="img" aria-label="Photo of a teacher helping children at a table"></div>
<div class="abs news" style="left:582px;top:861px">
  <div class="date">13 July, 2013</div>
  <div class="t">simply dummy text printing typesetting.</div>
  <div class="p">simply dummy text of the printing and typesetting industry. Lorem Ipsum has been the industry's standard dummy text.</div>
  <span class="more">Learn More ›</span>
</div>

<footer>
  <div class="abs footer"></div>
  <div class="abs fcol" style="left:90px"><div class="active">Reviews</div><div>Quick Tour</div><div>Pricing</div><div>Reviews</div><div>Quick Tour</div></div>
  <div class="abs fcol" style="left:246px;width:130px"><div>Graphic designer</div><div>Logo designer</div><div>Web designer</div><div>Print designer</div><div>Flyer designer</div></div>
  <div class="abs fcol" style="left:400px;width:150px"><div>How does it work?</div><div>How much does it cost?</div><div>How can I pay?</div><div>Writing a good design brief</div><div>FAQs</div></div>
  <div class="abs fcol" style="left:594px;top:1030px;width:96px"><div>Graphic designer</div><div>Logo designer</div><div>Web designer</div><div>Print designer</div><div>Flyer designer</div></div>
  <div class="abs bottom">Home &nbsp;|&nbsp; About Us &nbsp;|&nbsp; Careers &nbsp;|&nbsp; Terms &amp; Conditions &nbsp;|&nbsp; Contact<br>Copyright © 2012. All Rights Reserved.</div>
</footer>

</body>
</html>
```